We are a church and would like a flyer for a special service that is held once a quarter to get families and friends to come out to join us. See below content and details for sizes.
Church Name: Covenant Harvest Global Fellowship
Church Logo : Attached
Title : Family and Friends Day
Subtitle: Strengthening Families - Connecting Relationships
Host: Bishop Kwame Dantor (file attached. Don't need full body. Please crop)
Date: Sunday, 24 May
Time: 9:30 AM
Address: 2917 Marlow Lane, Suite F, Bowie MD, 20716
Phone : 240 593 2186
Website: www.chgfellowship.org
Flyer Size: Facebook size 851 x 314 pixels, Flash size 680 x 340 & Power Point size Standard

```html
<!DOCTYPE html>
<html lang="en">
<head>
<meta charset="utf-8">
<title>Family and Friends – Flash Banner</title>
<link rel="stylesheet" href="https://fonts.googleapis.com/css2?family=Quicksand:wght@300;400&family=Open+Sans:ital,wght@0,400;0,700;1,400&display=swap">
<style>
  :root {
    --page-bg: #e6e7e9;
    --label: #3a3a3a;
    --wood-dark: #3a1206;
    --wood-mid: #8a3f12;
    --wood-light: #c77a2c;
    --white: #ffffff;
    --cream: #fbeee0;
    --brand-blue: #1d3f7a;
    --photo-a: #6b625c;
    --photo-b: #3f3a37;
  }
  * { margin: 0; padding: 0; box-sizing: border-box; }
  html, body { width: 1200px; height: 786px; overflow: hidden; }
  body { background: var(--page-bg); position: relative; font-family: "Quicksand", sans-serif; }

  .size-label {
    position: absolute; top: 78px; left: 0; width: 1200px; text-align: center;
    font-family: "Open Sans", sans-serif; font-size: 46px; color: var(--label);
  }

  .banner {
    position: absolute; left: 105px; top: 168px; width: 972px; height: 487px;
    overflow: hidden; color: var(--white);
  }
  .banner__wood {
    position: absolute; inset: 0;
    background:
      radial-gradient(ellipse 45% 70% at 48% 40%, rgba(214,140,60,.75), transparent 70%),
      linear-gradient(90deg, var(--wood-dark) 0%, var(--wood-mid) 25%, var(--wood-light) 48%, var(--wood-mid) 75%, var(--wood-dark) 100%);
  }
  .banner__swoosh { position: absolute; inset: 0; }

  .host-photo {
    position: absolute; left: 0; top: 162px; width: 266px; height: 325px;
    background: linear-gradient(180deg, var(--photo-a), var(--photo-b));
    border-radius: 120px 120px 0 0;
  }

  .title { position: absolute; font-weight: 300; line-height: 1; letter-spacing: 1px; }
  .title--family { left: 168px; top: 4px; font-size: 104px; }
  .title--family .title__and { font-size: 50px; letter-spacing: 0; margin-left: -4px; }
  .title--friends { left: 215px; top: 112px; font-size: 104px; }

  .subtitle {
    position: absolute; left: 238px; top: 240px;
    font-size: 33px; font-weight: 400; line-height: 40px; color: var(--cream);
  }

  .event-details {
    position: absolute; right: 10px; top: 28px; text-align: right; font-weight: 400;
  }
  .event-details__date { font-size: 30px; line-height: 38px; }
  .event-details__time { font-size: 30px; line-height: 36px; }
  .event-details__address { font-size: 17px; line-height: 24px; }
  .event-details__phone { font-size: 25px; line-height: 28px; margin-top: 38px; }
  .event-details__web { font-size: 26px; line-height: 28px; }

  .host-name {
    position: absolute; left: 295px; top: 442px;
    font-family: "Open Sans", sans-serif; font-style: italic; font-size: 20px;
  }

  .church-name {
    position: absolute; right: 14px; top: 380px; width: 230px;
    display: flex; align-items: center; gap: 10px;
    color: var(--brand-blue); font-size: 19px; font-weight: 400; line-height: 23px; text-align: left;
  }
  .church-name__dot {
    flex: none; width: 34px; height: 34px; border-radius: 50%; background: var(--brand-blue);
  }
</style>
</head>
<body>
  <h1 class="size-label">Flash</h1>

  <section class="banner">
    <div class="banner__wood" role="img" aria-label="Warm brown wood-plank background"></div>
    <svg class="banner__swoosh" width="972" height="487" viewBox="0 0 972 487" aria-hidden="true">
      <path d="M425 487 C 640 445, 860 380, 972 275 L972 487 Z" fill="var(--white)"/>
    </svg>

    <div class="host-photo" role="img" aria-label="Portrait of Bishop Kwame Dantor in a grey suit jacket, smiling"></div>

    <h2 class="title title--family">Family<span class="title__and">and</span></h2>
    <h2 class="title title--friends">Friends</h2>

    <p class="subtitle">Strengthening Families<br>Connecting Relationships</p>

    <div class="event-details">
      <p class="event-details__date">Sunday, 24th May</p>
      <p class="event-details__time">9:30 AM</p>
      <p class="event-details__address">2917 Marlow Lane Suite F, Bowie MD, 20716</p>
      <p class="event-details__phone">Phone 240 593 2186</p>
      <p class="event-details__web">www.chgfellowship.org</p>
    </div>

    <p class="host-name">Bishop Kwame Dantor</p>

    <div class="church-name">
      <span class="church-name__dot"></span>
      <span>Covenant Harvest Global Fellowship</span>
    </div>
  </section>
</body>
</html>
```